Moths Carry Lanterns Under Fog (MCLUF) by Velkin*

Hip-Hop artist Velkin is inquiring designs to compliment their latest album release (MCLUF). The design must be of a high resolution for we intend to print physical albums with the selected image, both front back. We are looking for something along the lines of abstract. Vague yet colorful enough to captivate. We are looking for something imaginative and dream-like. Weird is good (Psychedelic). The album includes songs like; Copper Tango, Lanterns in Water, and KVMT; to help identify the theme of work. Attached is a previous Velkin album cover. No text is necessary on the finalized image. I've also included a link to Velkin's latest work. Maybe it'll help. https://www.vidstreamly.net/clip?id=Q7pLm2Xa9Tk

Target Market(s)

Velkin's target demographic are both male and female between the ages of 18-35. This is typically the target market for fans of Hip Hop, Rap, Urban, etc.

Industry/Entity Type

Entertainment Industry

Other font styles liked:
• No Text Necessary Unless Requested

Colors

Designer to choose colors to be used in the design.

Requirements
Must have
• Color that captivates backed by originality. The image must be of high resolution. Requires the designing artist to be imaginative on a level of abstraction. Subjective elements are welcome. Cartoon-like also welcome. Comical is also welcome.
Nice to have
• We welcome qualities of obscure, odd, and the alternative. We welcome an alien technique over the traditional aesthetics of art. It must still qualify as beautiful by some standard. Incorporating geometry in some way might be a nice touch. The image must be balanced. Velkin has a high favoritism towards painters such as Tobin Marsh. Particularly the vibrant colors and subliminal imaging. Revolution!
Should not have
• Velkin is not particular about what shouldn't qualify. As artists ourselves, we welcome all types of innovation. We do ask you please avoid stock images. Original work.

```html
<!DOCTYPE html>
<html lang="en">
<head>
<meta charset="utf-8">
<title>MCLUF — Velkin</title>
<link rel="stylesheet" href="https://fonts.googleapis.com/css2?family=Rubik+Dirt&family=Work+Sans:ital,wght@1,300&display=swap">
<style>
  :root {
    --night: #0c0a16;
    --deep-blue: #0d2a55;
    --electric-blue: #1f8fd6;
    --ember: #a3260f;
    --amber: #d9661e;
    --lime: #8fd13a;
    --ink-white: #f4f1ec;
    --frame-warm: #c9a888;
    --frame-cool: #2d4058;
  }
  html, body {
    margin: 0;
    padding: 0;
    width: 1200px;
    height: 1200px;
    overflow: hidden;
    background: var(--night);
  }
  .album-cover {
    position: relative;
    width: 1200px;
    height: 1200px;
    overflow: hidden;
  }
  .night-photo {
    position: absolute;
    inset: 0;
    background:
      radial-gradient(ellipse 360px 160px at 820px 990px, var(--lime) 0%, rgba(143,209,58,0.55) 45%, transparent 75%),
      radial-gradient(ellipse 520px 260px at 480px 560px, var(--electric-blue) 0%, rgba(31,143,214,0.5) 45%, transparent 75%),
      radial-gradient(ellipse 240px 120px at 470px 330px, rgba(31,143,214,0.7) 0%, transparent 75%),
      radial-gradient(ellipse 700px 240px at 300px 540px, rgba(163,38,15,0.75) 0%, transparent 70%),
      radial-gradient(ellipse 600px 260px at 960px 640px, rgba(217,102,30,0.55) 0%, transparent 70%),
      radial-gradient(ellipse 760px 200px at 600px 1140px, rgba(163,38,15,0.85) 0%, transparent 75%),
      linear-gradient(180deg, var(--night) 0%, #130d24 40%, #1a0d14 70%, #200c0e 100%);
  }
  .cover-art {
    position: absolute;
    inset: 0;
  }
  .frame-line {
    fill: none;
    stroke: url(#frameGradient);
    stroke-width: 7;
  }
  .title-mark {
    font-family: "Rubik Dirt", "Impact", sans-serif;
    font-size: 190px;
    fill: var(--ink-white);
  }
  .artist-name {
    position: absolute;
    left: 0;
    right: 0;
    top: 578px;
    text-align: center;
    font-family: "Work Sans", "Helvetica Neue", sans-serif;
    font-style: italic;
    font-weight: 300;
    font-size: 34px;
    letter-spacing: 1px;
    color: var(--ink-white);
    margin: 0;
  }
</style>
</head>
<body>
  <main class="album-cover">
    <div class="night-photo" role="img" aria-label="Blurred night photograph of palm fronds in electric blue light over warm orange lamps and a glowing green pool"></div>

    <svg class="cover-art" width="1200" height="1200" viewBox="0 0 1200 1200" aria-hidden="false">
      <defs>
        <linearGradient id="frameGradient" x1="0" y1="0" x2="1" y2="1">
          <stop offset="0" stop-color="var(--frame-warm)"/>
          <stop offset="0.55" stop-color="var(--frame-cool)"/>
          <stop offset="1" stop-color="var(--frame-warm)"/>
        </linearGradient>
      </defs>

      <rect class="frame-line" x="46" y="34" width="1124" height="1136"/>

      <text class="title-mark" x="0" y="140" textLength="462" lengthAdjust="spacingAndGlyphs">MCLUF</text>
      <text class="title-mark" transform="translate(1058 0) rotate(90)" x="0" y="0" textLength="456" lengthAdjust="spacingAndGlyphs">MCLUF</text>
      <text class="title-mark" transform="translate(142 1200) rotate(-90)" x="0" y="0" textLength="480" lengthAdjust="spacingAndGlyphs">MCLUF</text>
      <text class="title-mark" transform="translate(1200 1058) rotate(180)" x="0" y="0" textLength="462" lengthAdjust="spacingAndGlyphs">MCLUF</text>
    </svg>

    <p class="artist-name">VELKIN</p>
  </main>
</body>
</html>
```